Author/ Speaker Business Card design

I need a business card designed that will go with the branding that is already on my book and website. I like clean and straightforward, but I am not opposed to something more 'innovative'.

Target Market(s)

Colleges and Universities, educational institutions

Industry/Entity Type

Education

Contact Information for Business Card

Standard size. It should be able to be printed on good quality white or ivory paper.

Font styles to use
Sans Serif

Colors
0355a3

Requirements
Must have
• There's a blue on my website. It should have some blue. My logo is at the top. It should have the logo incorporated somewhere on it. My name, Author | Speaker | Teacher | Trainer, my phone number (+31 64-207 5819), my email address (milo@theboldlearner.example), Social media icons (twitter, Instagram, LinkedIn) with the addresses (twitter @writermilofenwick, Instagram - theboldlearner, LinkedIn - theboldlearner) By they way, the website is www.theboldlearner.example. There is a photo of the book on the website. Also, my full name is Milo Fenwick
Nice to have
• Try to use the font that is on the website and book. Also, if you could get that blue, that would be great.
Should not have
• My photo

```html
<!DOCTYPE html>
<html lang="en">
<head>
<meta charset="utf-8">
<title>The Bold Learner – Business Card</title>
<link rel="stylesheet" href="https://fonts.googleapis.com/css2?family=Montserrat:wght@700&family=Open+Sans:wght@400;600&display=swap">
<style>
  :root {
    --brand-blue: #0355a3;
    --card-blue: #0b4fb0;
    --paper: #f4f4f2;
    --ink: #3a3a3a;
    --rule: #d4d6d8;
    --backdrop: #cfd3d4;
  }
  * { box-sizing: border-box; margin: 0; padding: 0; }
  html, body { width: 1200px; height: 1050px; overflow: hidden; }
  body {
    background: var(--backdrop);
    font-family: "Open Sans", Arial, sans-serif;
    color: var(--ink);
    position: relative;
  }
  .card {
    position: absolute;
    left: 250px;
    width: 700px;
    height: 400px;
    box-shadow: 0 6px 18px rgba(0,0,0,0.12);
  }
  .card--front { top: 90px; background: var(--paper); }
  .card--back { top: 560px; background: var(--card-blue); }

  .brand-name {
    font-family: "Montserrat", Arial, sans-serif;
    font-weight: 700;
    display: flex;
    align-items: center;
    gap: 12px;
    letter-spacing: 0.5px;
  }
  .brand-name__mark { width: 18px; height: 18px; border-radius: 50%; }

  .card--front .brand-name {
    position: absolute; top: 62px; right: 56px;
    color: var(--brand-blue); font-size: 30px;
  }
  .card--front .brand-name__mark { background: var(--brand-blue); }

  .card--back .brand-name {
    position: absolute; top: 50%; left: 50%;
    transform: translate(-50%, -50%);
    color: #e9edf3; font-size: 38px;
  }
  .card--back .brand-name__mark { background: #e9edf3; width: 22px; height: 22px; }

  .identity { position: absolute; left: 56px; top: 150px; width: 420px; }
  .identity__name {
    font-family: "Montserrat", Arial, sans-serif;
    font-weight: 700; font-size: 24px; color: var(--brand-blue);
    letter-spacing: 1px; text-transform: uppercase;
  }
  .identity__roles { font-size: 15px; margin-top: 4px; }
  .identity__rule { height: 1px; background: var(--rule); margin: 14px 0 14px; }

  .contact-list { list-style: none; font-size: 15px; }
  .contact-list li { display: flex; align-items: center; gap: 10px; line-height: 26px; }
  .contact-list svg { width: 15px; height: 15px; flex: none; }

  .social {
    position: absolute; right: 56px; bottom: 44px; width: 250px;
    border-top: 1px solid var(--rule); padding-top: 12px;
  }
  .social ul { list-style: none; font-size: 15px; }
  .social li { display: flex; align-items: center; gap: 10px; line-height: 25px; }
  .social__square { width: 14px; height: 14px; background: var(--brand-blue); flex: none; }
</style>
</head>
<body>

<section class="card card--front" aria-label="Card front">
  <div class="brand-name"><span class="brand-name__mark"></span>The Bold Learner</div>

  <div class="identity">
    <h1 class="identity__name">Milo Fenwick</h1>
    <p class="identity__roles">Author • Speaker • Teacher • Trainer</p>
    <div class="identity__rule"></div>
    <ul class="contact-list">
      <li>
        <svg viewBox="0 0 16 16" aria-hidden="true"><path d="M3 1.5l3 .5 1 3.2-1.8 1.2a8 8 0 0 0 4.4 4.4L10.8 9l3.2 1 .5 3-2 1.5C7 14.5 1.5 9 1.5 3.5z" fill="none" stroke="var(--brand-blue)" stroke-width="1.4" stroke-linejoin="round"/></svg>
        +31 64-207 5819
      </li>
      <li>
        <svg viewBox="0 0 16 16" aria-hidden="true"><rect x="1.5" y="3.5" width="13" height="9" fill="none" stroke="var(--brand-blue)" stroke-width="1.4"/><path d="M1.5 3.5L8 9l6.5-5.5" fill="none" stroke="var(--brand-blue)" stroke-width="1.4"/></svg>
        milo@theboldlearner.example
      </li>
      <li>
        <svg viewBox="0 0 16 16" aria-hidden="true"><circle cx="8" cy="8" r="6.5" fill="none" stroke="var(--brand-blue)" stroke-width="1.3"/><ellipse cx="8" cy="8" rx="2.8" ry="6.5" fill="none" stroke="var(--brand-blue)" stroke-width="1.1"/><path d="M1.5 8h13" stroke="var(--brand-blue)" stroke-width="1.1"/></svg>
        www.theboldlearner.example
      </li>
    </ul>
  </div>

  <div class="social">
    <ul>
      <li><span class="social__square"></span>@writermilofenwick</li>
      <li><span class="social__square"></span>theboldlearner</li>
      <li><span class="social__square"></span>theboldlearner</li>
    </ul>
  </div>
</section>

<section class="card card--back" aria-label="Card back">
  <div class="brand-name"><span class="brand-name__mark"></span>The Bold Learner</div>
</section>

</body>
</html>
```